Web Developer Wordpress theme

I'm a web developer but a poor designer so i need somebody to design me a cool and professional WordPress theme. I specialize in shopping cart developments and modifications as well as hosting for these system so would like the design to show this off. I am UK based and want this to also come across in the design.
As for colors and layout i am open mined just use your imaginantion i will let know what i think of your designs.
also forgot to mention my business name is travolek
and my exsiting site is travolek.co.uk

```html
<!DOCTYPE html>
<html lang="en">
<head>
<meta charset="utf-8">
<title>travolek – serious web development</title>
<link rel="stylesheet" href="https://fonts.googleapis.com/css2?family=Source+Sans+3:wght@400;600;700&family=Arimo:wght@400&display=swap">
<style>
:root{
  --black:#000;
  --orange:#ff8a1e;
  --orange-deep:#f47a0c;
  --panel:#1f2327;
  --panel-light:#2c3136;
  --nav-text:#3fb4e6;
  --heading-blue:#2aa3d4;
  --white:#fff;
  --text-grey:#555;
  --text-dark:#222;
  --banner-red:#6e0a1c;
  --banner-red-dark:#3e0410;
  --quote-red:#b8440e;
  --green:#9ccc2a;
  --footer-text:#9aa0a6;
  --price-box:#1e2226;
}
*{box-sizing:border-box;margin:0;padding:0}
html,body{width:1120px;height:1200px;overflow:hidden}
body{
  position:relative;
  background:linear-gradient(180deg,var(--black) 0,#0b0b0b 130px,#3a3a3a 200px,var(--orange) 200px,var(--orange-deep) 1200px);
  font-family:"Source Sans 3",sans-serif;
}
.abs{position:absolute}
.brand{left:193px;top:74px;color:var(--orange);font-size:50px;font-weight:600;line-height:1;letter-spacing:-1px}
.brand-tag{left:258px;top:129px;color:#aaa;font-size:10px;letter-spacing:2px}
.login{left:870px;top:130px;width:62px;height:22px;border-radius:6px;background:linear-gradient(#5cc4f0,#2a97cf);color:#0d3550;font-size:11px;font-weight:700;text-align:center;line-height:22px;border:1px solid #86d6f7}
.nav{left:176px;top:162px;width:768px;height:40px;background:linear-gradient(#32373c,#1c1f22);border-radius:4px 4px 0 0;display:flex}
.nav a{color:var(--nav-text);font-size:11px;font-weight:700;text-decoration:none;line-height:40px;padding:0 17px;border-right:1px solid #15181a;letter-spacing:.3px}
.nav a:first-child{width:68px}
.nav a:nth-child(2){width:80px;text-align:center}
.search{left:756px;top:169px;width:180px;height:24px;background:#16191c;border:1px solid #444;border-radius:2px}
.banner{left:176px;top:202px;width:768px;height:224px;background:linear-gradient(90deg,var(--banner-red),#8a1024 60%,var(--banner-red-dark));border:1px solid #ccc;overflow:hidden}
.banner-art{left:460px;top:0;width:308px;height:224px;background:radial-gradient(circle at 50% 45%,#d8d8e0 0,#b03068 30%,#5a1030 70%,transparent 100%)}
.banner-title{left:201px;top:284px;color:var(--white);font-size:40px;font-weight:600;letter-spacing:-.5px}
.banner-copy{left:191px;top:334px;width:492px;height:78px;background:rgba(20,10,12,.75);border-radius:4px;color:#eee;font-size:10px;line-height:14.5px;padding:11px 11px}
.slider-bar{left:176px;top:425px;width:768px;height:20px;background:linear-gradient(#2a2f34,#15181b)}
.content{left:176px;top:445px;width:768px;height:540px;background:var(--white)}
.col-title{font-size:19px;font-weight:600;color:var(--text-dark);top:479px}
.col-text{top:513px;width:232px;font-size:9.3px;line-height:14.5px;color:var(--text-grey)}
.product{top:586px;width:225px;height:92px;border:1px solid #ccc;background:#f2f2f2}
.product-img{position:absolute;left:5px;top:5px;width:150px;height:80px}
.price{position:absolute;right:9px;top:8px;width:60px;height:74px;background:var(--price-box);border-radius:4px;color:#fff;text-align:center}
.price b{display:block;font-size:19px;margin-top:8px;line-height:20px}
.price i{display:block;font-style:normal;font-size:10px;font-weight:700}
.price span{position:absolute;left:2px;right:2px;bottom:3px;height:16px;border-radius:3px;font-size:8px;line-height:16px;font-weight:700}
.sec-title{top:710px;color:var(--heading-blue);font-size:15px;font-weight:400}
.body-text{font-family:Arimo,Arial,sans-serif;font-size:10px;line-height:14.5px;color:var(--text-dark)}
.svc-icon{width:32px;height:32px;border:1px solid #ccc;background:#eee;border-radius:2px}
.quote-by{color:var(--quote-red)}
.more{left:805px;top:949px;width:125px;height:21px;border-radius:5px;background:linear-gradient(#b6e04a,#86b81e);color:#24400a;font-size:11px;font-weight:700;text-align:center;line-height:21px}
.footer{left:176px;top:985px;width:768px;height:196px;background:linear-gradient(#2c3136,#1a1d20);border-radius:0 0 4px 4px}
.foot-title{top:996px;color:var(--heading-blue);font-size:15px;letter-spacing:.5px}
.foot-rule{left:176px;top:1024px;width:768px;height:1px;background:#3c4248}
.foot-list{top:1036px;list-style:none;font-size:9px;line-height:16px;color:var(--footer-text)}
.foot-list li::before{content:"▸ ";font-size:8px}
.contact{left:768px;top:1034px;font-size:9.5px;line-height:17px;color:var(--footer-text)}
.contact li{list-style:none;display:flex;align-items:center;gap:12px}
.contact svg{width:13px;height:13px}
.socials{display:flex;gap:2px}
.socials i{width:12px;height:12px;border-radius:2px;display:block}
.foot-brand{left:473px;top:1099px;width:162px;height:50px;background:#000;color:var(--orange);font-size:28px;font-weight:600;text-align:center;line-height:46px}
.copyright{left:0;width:1120px;top:1158px;text-align:center;color:#ddd;font-size:9px;letter-spacing:.3px}
</style>
</head>
<body>
<header>
  <div class="abs brand">travolek</div>
  <div class="abs brand-tag">serious web development</div>
  <div class="abs login">LOGIN</div>
  <nav class="abs nav">
    <a href="#">Home</a><a href="#">Services</a><a href="#">Addons</a><a href="#">Our E-commerce Hosting</a><a href="#">Blog</a><a href="#">Contact</a>
  </nav>
  <div class="abs search">
    <svg class="abs" style="left:158px;top:4px" width="15" height="15" viewBox="0 0 15 15"><circle cx="6" cy="6" r="4.5" fill="none" stroke="#aaa" stroke-width="1.6"/><line x1="9.3" y1="9.3" x2="13.5" y2="13.5" stroke="#aaa" stroke-width="2"/></svg>
  </div>
</header>

<section>
  <div class="abs banner">
    <div class="abs banner-art" role="img" aria-label="Colourful shopping cart filled with bags and balloons against a city skyline"></div>
  </div>
  <h1 class="abs banner-title">UK Freelance Web Deveoper</h1>
  <p class="abs banner-copy">Freelance web developer avaliable for hire, Specializing in Vendora shopping cart and creating addons and customized templates. I have been a freelance developer for over 5 years now and complete all sizes of projects starting out on Hire-a-coder doing small project then going on to the larger projects.</p>
  <div class="abs slider-bar">
    <svg class="abs" style="left:362px;top:4px" width="46" height="12" viewBox="0 0 46 12"><g fill="#333" stroke="#888"><circle cx="6" cy="6" r="5"/><circle cx="17" cy="6" r="5"/><circle cx="28" cy="6" r="5"/><circle cx="39" cy="6" r="5"/></g></svg>
  </div>
</section>

<main>
  <div class="abs content"></div>

  <h2 class="abs col-title" style="left:193px">Vendora Addons</h2>
  <p class="abs col-text" style="left:193px">We create addon and modules to work with the vendora shopping cart system. If you just want a new payment gateway or more detailed reports Just ask and we will help.</p>
  <div class="abs product" style="left:190px">
    <div class="product-img" role="img" aria-label="Row of colourful shopping bags" style="background:linear-gradient(90deg,#f04a2a,#f0409a,#9ad040,#2a8ae0,#1ab0c0)"></div>
    <div class="price"><b>£90*</b><i>*From</i><span style="background:#d81a1a">ORDER NOW!</span></div>
  </div>

  <h2 class="abs col-title" style="left:449px">Vendora Templates</h2>
  <p class="abs col-text" style="left:449px">So you have the best shopping cart software Now you just need it styled let us help you get your shopping cart to match you requirements, Using all the latest technologies we can bring your business to the leading edge.</p>
  <div class="abs product" style="left:446px">
    <div class="product-img" role="img" aria-label="Screenshot of a clothing store template" style="background:linear-gradient(#222 0,#222 15%,#f4f4f4 15%,#e6e6e6)"></div>
    <div class="price"><b>£400*</b><i>*From</i><span style="background:#1d5f9a">ORDER NOW!</span></div>
  </div>

  <h2 class="abs col-title" style="left:704px">Shopping Cart Software</h2>
  <p class="abs col-text" style="left:704px">Not happy with your shopping cart or just require more features then speak to us. We use vendora shopping cart and customize it to fit you needs. Purchase the shopping cart throught us and you also get to choose 2 addons free and a discounted template design</p>
  <div class="abs product" style="left:701px">
    <div class="product-img" role="img" aria-label="Red and white software box" style="left:12px;width:68px;background:linear-gradient(135deg,#f2f2f2,#d8261e 55%,#a01010)"></div>
    <div class="price"><b>£350*</b><i>*From</i><span style="background:#ddd;color:#222">ORDER NOW!</span></div>
  </div>

  <h3 class="abs sec-title" style="left:200px">Welcome</h3>
  <p class="abs body-text" style="left:198px;top:741px;width:225px">travolek, is a freelance web developer specializing in online shopping cart solution whether it is just a simple PayMint cart or a full blown shopping management system we customize and style it to your requirements</p>

  <h3 class="abs sec-title" style="left:470px">Services</h3>
  <svg class="abs svc-icon" style="left:462px;top:738px" viewBox="0 0 32 32"><rect x="9" y="6" width="14" height="20" fill="#cfd8e0" stroke="#6a7a8a"/><line x1="11" y1="11" x2="21" y2="11" stroke="#6a7a8a"/><line x1="11" y1="15" x2="21" y2="15" stroke="#6a7a8a"/></svg>
  <p class="abs body-text" style="left:503px;top:741px;width:190px">Fast and Secure web hosting Servers to support your e-commerce solution</p>
  <svg class="abs svc-icon" style="left:462px;top:787px" viewBox="0 0 32 32"><path d="M6 9h4l3 11h11l2-8H11" fill="none" stroke="#666" stroke-width="1.5"/><circle cx="14" cy="24" r="1.8" fill="#666"/><circle cx="22" cy="24" r="1.8" fill="#666"/></svg>
  <p class="abs body-text" style="left:503px;top:787px;width:190px">Specialize in shopping cart solutions and customizing them to meet your needs</p>
  <svg class="abs svc-icon" style="left:462px;top:834px" viewBox="0 0 32 32"><circle cx="16" cy="16" r="10" fill="#e0a030"/><path d="M16 6a10 10 0 0 1 10 10H16z" fill="#3a8ad8"/><path d="M16 16h10a10 10 0 0 1-10 10z" fill="#d83a6a"/><path d="M16 16v10A10 10 0 0 1 6 16z" fill="#4ac04a"/></svg>
  <p class="abs body-text" style="left:503px;top:834px;width:190px">Design your online store to make it comfortable and easy for your customers to browser and purchase</p>

  <h3 class="abs sec-title" style="left:721px">Our Customers Say</h3>
  <p class="abs body-text" style="left:726px;top:741px;width:190px">" Great good completed a re work on our exsiting site was really please. "<br><span class="quote-by">Karen Mallory, Teacupbritain.com</span></p>
  <p class="abs body-text" style="left:716px;top:798px;width:200px">&nbsp;&nbsp;&nbsp;" carried out what we thought was a complex piece of scripting on our Vendora website He completed the work quickly, well within agreed timescales - it was accurate and most importantly on agreed budget. We intend to use his skills for all future development on the site and he comes highly recommended by Quick Trivia Many thanks "<br><span class="quote-by">&nbsp;&nbsp;&nbsp;Peter Lowe, www.quick-trivia.co.uk</span></p>
  <div class="abs more">more testimonials..</div>
</main>

<footer>
  <div class="abs footer"></div>
  <div class="abs foot-rule"></div>
  <h4 class="abs foot-title" style="left:198px">Control</h4>
  <ul class="abs foot-list" style="left:200px"><li>Log in</li><li>Entries RSS</li><li>Comments RSS</li><li>Blogpress.org</li></ul>
  <h4 class="abs foot-title" style="left:390px">Recent Posts</h4>
  <ul class="abs foot-list" style="left:391px"><li>Out of Stock Notification</li><li>At Last a HOME</li></ul>
  <h4 class="abs foot-title" style="left:578px">Tag</h4>
  <p class="abs foot-list" style="left:578px">travolek Web Development</p>
  <h4 class="abs foot-title" style="left:768px">Get in Touch</h4>
  <ul class="abs contact">
    <li><svg viewBox="0 0 13 13"><path d="M2 4c0-2 9-2 9 0v2H9V5H4v1H2z M3 7h7v4H3z" fill="#888"/></svg>1-800-555-5555</li>
    <li><svg viewBox="0 0 13 13"><rect x="1" y="3" width="11" height="7" fill="#888"/><path d="M1 3l5.5 4L12 3" fill="none" stroke="#333"/></svg>info@travolek.co.uk</li>
    <li><svg viewBox="0 0 13 13"><path d="M2 11l1-3 6-6 2 2-6 6z" fill="#888"/></svg>Contact Form</li>
    <li><svg viewBox="0 0 13 13"><circle cx="6.5" cy="6.5" r="5" fill="#888"/></svg>YourChatUserID</li>
    <li><svg viewBox="0 0 13 13"><path d="M3 10l7-7M4 6l-2 2 3 3 2-2M9 7l2-2-3-3-2 2" fill="none" stroke="#888" stroke-width="1.5"/></svg>
      <span class="socials"><i style="background:#f08a1a"></i><i style="background:#3aa8e0"></i><i style="background:#3b5998"></i><i style="background:#5a7ab0"></i><i style="background:#e0e0e0"></i><i style="background:#1a74b0"></i></span></li>
  </ul>
  <div class="abs foot-brand">travolek</div>
  <p class="abs copyright">Website content Copyrighted travolek 2012</p>
</footer>
</body>
</html>
```